Health Information/Education Logo Design

We need a logo design for a new company based in Atlanta called Brightpath Care. The program is about patient empowerment. We provide health information and education on how to get healthy, stay healthy, and how to be proactive in your care. We also provide medication and injection training to help patients feel their best and to ensure successful therapy outcomes.
We like the colors yellow, pink, teal and purple and would like to see some or all of these colors in the designs. The final design should communicate caring, considerate, compassionate information, education and training services
Education
Contact Information for Business Card
Brightpath Care
Lorraine Pettaway RN, MSN, MHA
Nurse Educator
404.555.0187 cell
404.555.0142 fax

```html
<!DOCTYPE html>
<html lang="en">
<head>
<meta charset="utf-8">
<title>Brightpath Care – Business Card</title>
<link href="https://fonts.googleapis.com/css2?family=Poppins:wght@400;600&display=swap" rel="stylesheet">
<style>
  :root {
    --page-bg: #ecebef;
    --card-white: #ffffff;
    --purple-light: #a59fd0;
    --purple-mid: #9a92cb;
    --purple-deep: #8c80c2;
    --brand-purple: #8e84c4;
    --accent-yellow: #e2cd17;
    --text-light: #ffffff;
  }
  html, body {
    margin: 0;
    padding: 0;
    width: 1200px;
    height: 1000px;
    overflow: hidden;
    background: var(--page-bg);
    font-family: "Poppins", sans-serif;
  }
  .business-card {
    position: absolute;
    left: 100px;
    top: 210px;
    width: 1000px;
    height: 580px;
    border-radius: 44px;
    overflow: hidden;
    background: var(--card-white);
    box-shadow: 0 10px 30px rgba(60, 50, 90, 0.18);
  }
  .card-shapes {
    position: absolute;
    inset: 0;
  }
  .brand-lockup {
    position: absolute;
    left: 70px;
    top: 110px;
    display: flex;
    align-items: center;
    gap: 18px;
  }
  .brand-dot {
    width: 26px;
    height: 26px;
    border-radius: 50%;
    background: var(--accent-yellow);
  }
  .brand-name {
    font-weight: 600;
    font-size: 52px;
    color: var(--brand-purple);
    letter-spacing: -0.5px;
    line-height: 1;
  }
  .contact-block {
    position: absolute;
    right: 60px;
    top: 350px;
    text-align: right;
    color: var(--text-light);
  }
  .person-name {
    font-weight: 600;
    font-size: 44px;
    line-height: 1.05;
    letter-spacing: -0.3px;
  }
  .person-title {
    font-weight: 400;
    font-size: 27px;
    margin-top: 4px;
  }
  .phone-line {
    margin-top: 44px;
    font-size: 27px;
    display: flex;
    justify-content: flex-end;
    align-items: center;
    gap: 8px;
  }
  .phone-divider {
    color: var(--accent-yellow);
    margin: 0 10px;
  }
  .phone-icon {
    width: 18px;
    height: 24px;
  }
</style>
</head>
<body>
  <div class="business-card">
    <svg class="card-shapes" width="1000" height="580" viewBox="0 0 1000 580" aria-hidden="true">
      <defs>
        <linearGradient id="purpleField" x1="0" y1="0" x2="1" y2="0.4">
          <stop offset="0" stop-color="var(--purple-deep)"/>
          <stop offset="0.5" stop-color="var(--purple-light)"/>
          <stop offset="1" stop-color="var(--purple-deep)"/>
        </linearGradient>
      </defs>
      <path class="accent-stripe" d="M640 0 Q520 380 96 580 L134 580 Q548 380 662 0 Z" fill="var(--accent-yellow)"/>
      <path class="purple-field" d="M662 0 Q548 380 134 580 L1000 580 L1000 0 Z" fill="url(#purpleField)"/>
    </svg>

    <div class="brand-lockup">
      <span class="brand-dot"></span>
      <span class="brand-name">Brightpath Care</span>
    </div>

    <div class="contact-block">
      <div class="person-name">Lorraine Pettaway</div>
      <div class="person-title">RN, MSN, MHA Nurse Educator</div>
      <div class="phone-line">
        <svg class="phone-icon" viewBox="0 0 18 24" aria-label="cell">
          <rect x="3" y="1" width="12" height="22" rx="2" fill="none" stroke="var(--accent-yellow)" stroke-width="2"/>
          <circle cx="9" cy="19" r="1.4" fill="var(--accent-yellow)"/>
        </svg>
        <span class="phone-number">404.555.0187</span>
        <span class="phone-divider">|</span>
        <span class="phone-number">404.555.0142</span>
        <svg class="phone-icon" viewBox="0 0 22 24" style="width:22px" aria-label="fax">
          <rect x="5" y="2" width="12" height="8" fill="none" stroke="var(--accent-yellow)" stroke-width="2"/>
          <rect x="1" y="10" width="20" height="10" rx="2" fill="none" stroke="var(--accent-yellow)" stroke-width="2"/>
          <rect x="6" y="16" width="10" height="6" fill="var(--accent-yellow)"/>
        </svg>
      </div>
    </div>
  </div>
</body>
</html>
```